Business Card for Voltrix

Horizontal business card for voltrix, the electrical contractor.
clean and professional looking, using company branding and colours.
I also want the blue in the logo and wording to be made a more 'electric' blue and the grey 'Voltrix' to be slightly darker.

Pleas use the following contact details:

Colin Marsh
Owner

t: 01736 582910
m: 07831 206719
e: colin@voltrix-installs.co.uk

www.voltrix-installs.co.uk

Industry/Entity Type

Electrical

Font styles to use
Sans Serif

```html
<!DOCTYPE html>
<html lang="en">
<head>
<meta charset="utf-8">
<title>Voltrix business card</title>
<link rel="stylesheet" href="https://fonts.googleapis.com/css2?family=Open+Sans:wght@400;600;700&display=swap">
<style>
  :root {
    --stage: #eeeeee;
    --stage-light: #ffffff;
    --card-edge: #5a5a5a;
    --card-white: #ffffff;
    --card-grey: #d4d6d8;
    --card-grey-light: #f7f7f7;
    --ink: #222222;
    --ink-soft: #444444;
    --brand-grey: #5d666c;
    --electric-blue: #0a8fdc;
    --icon-red: #b5121b;
    --strip-dark: #b9bbbe;
    --strip-light: #ffffff;
  }
  * { margin: 0; padding: 0; box-sizing: border-box; }
  html, body { width: 1200px; height: 1200px; overflow: hidden; }
  body {
    position: relative;
    font-family: "Open Sans", sans-serif;
    background: radial-gradient(circle at 50% 50%, var(--stage-light) 0%, var(--stage-light) 35%, var(--stage) 80%);
  }
  .card {
    position: absolute;
    left: 245px;
    width: 708px;
    height: 456px;
    border: 1.3px solid var(--card-edge);
    overflow: hidden;
  }
  .card-front {
    top: 131px;
    background: var(--card-white);
    border-radius: 0 38px 0 38px;
  }
  .card-back {
    top: 601px;
    border-radius: 38px 0 38px 0;
    background: radial-gradient(ellipse at 50% 40%, var(--card-grey-light) 0%, var(--card-grey) 85%);
  }
  .side-strip {
    position: absolute;
    left: 0; top: 0;
    width: 74px; height: 100%;
    background: linear-gradient(90deg, var(--strip-dark) 0%, var(--strip-light) 100%);
  }
  .side-url {
    position: absolute;
    left: 33px; top: 96px;
    writing-mode: vertical-rl;
    font-size: 17px;
    color: var(--ink);
    letter-spacing: 0.2px;
  }
  .holder { position: absolute; left: 111px; top: 52px; }
  .holder-name { font-size: 20px; font-weight: 700; color: var(--ink); line-height: 1.1; }
  .holder-role { font-size: 17px; color: var(--ink-soft); line-height: 1.15; }
  .brand-disc {
    position: absolute;
    left: 242px; top: 98px;
    width: 250px; height: 250px;
    border-radius: 50%;
    background: var(--electric-blue);
  }
  .contacts {
    position: absolute;
    right: 34px; top: 326px;
    list-style: none;
    text-align: right;
    font-size: 17px;
    color: var(--ink-soft);
  }
  .contacts li { display: flex; justify-content: flex-end; align-items: center; gap: 8px; height: 25px; }
  .contacts li.email { margin-top: 4px; }
  .contacts svg { width: 18px; height: 18px; fill: var(--icon-red); }
  .lockup-disc {
    position: absolute;
    left: 46px; top: 166px;
    width: 78px; height: 78px; border-radius: 50%;
    background: var(--electric-blue);
  }
  .lockup-name {
    position: absolute;
    left: 133px; top: 172px;
    font-size: 50px; font-weight: 600;
    letter-spacing: 38px;
    color: var(--brand-grey);
    line-height: 1;
    white-space: nowrap;
  }
  .tagline {
    position: absolute;
    left: 136px; top: 226px;
    font-size: 24px;
    line-height: 1;
    letter-spacing: 4.6px;
    color: var(--electric-blue);
    white-space: nowrap;
  }
  .back-url {
    position: absolute;
    left: 0; right: 0; top: 414px;
    text-align: center;
    font-size: 18px;
    color: var(--ink);
  }
</style>
</head>
<body>
  <section class="card card-front">
    <div class="side-strip"></div>
    <p class="side-url">www.voltrix-installs.co.uk</p>
    <div class="holder">
      <p class="holder-name">Colin Marsh</p>
      <p class="holder-role">Owner</p>
    </div>
    <div class="brand-disc"></div>
    <ul class="contacts">
      <li>01736 582910
        <svg viewBox="0 0 24 24" aria-hidden="true"><path d="M6.6 10.8a15.1 15.1 0 0 0 6.6 6.6l2.2-2.2a1 1 0 0 1 1-.25 11.4 11.4 0 0 0 3.6.57 1 1 0 0 1 1 1V20a1 1 0 0 1-1 1A17 17 0 0 1 3 4a1 1 0 0 1 1-1h3.5a1 1 0 0 1 1 1 11.4 11.4 0 0 0 .57 3.6 1 1 0 0 1-.25 1z"/></svg>
      </li>
      <li>07831 206719
        <svg viewBox="0 0 24 24" aria-hidden="true"><path d="M7 1h10a2 2 0 0 1 2 2v18a2 2 0 0 1-2 2H7a2 2 0 0 1-2-2V3a2 2 0 0 1 2-2zm1 3v8h8V4zm0 10v2h2v-2zm3 0v2h2v-2zm3 0v2h2v-2zm-6 3v2h2v-2zm3 0v2h2v-2zm3 0v2h2v-2z"/></svg>
      </li>
      <li class="email">colin@voltrix-installs.co.uk
        <svg viewBox="0 0 24 24" aria-hidden="true"><path d="M2 5h20v14H2zm2 2v.4l8 5.2 8-5.2V7zm0 2.8V17h16V9.8l-8 5.2z"/></svg>
      </li>
    </ul>
  </section>

  <section class="card card-back">
    <span class="lockup-disc"></span>
    <p class="lockup-name">VOLTRIX</p>
    <p class="tagline">THE ELECTRICAL CONTRACTOR</p>
    <p class="back-url">www.voltrix-installs.co.uk</p>
  </section>
</body>
</html>
```